Website Redesign for Asset Management

We need a full redesign on the website for Velbrook Asset Management. Velbrook is an asset manager that manages both long - only products and alternative investments. We would like to see a clean and innovative website that showcases the products of the firm and the management of the firm.
www.velbrook-example.com
Updates

Output should be in PSD and designer should have groups/layers for the developer to extract the imagesĀ 

Feel free to play with the colours as we are not stuck to current colours.

Target Market(s)

The target market are affluent individuals, pensions, foundations and endowments

Industry/Entity Type

Asset Management

Requirements
Must have
• We like the websites
www.dalvertcourt-example.com
www.quillanfunds-example.com
DO LIKE
http://www.morvatek-example.com/#Home
http://www.dalvertcourt-example.com/who-we-are/principals.html
http://www.ktrellin-example.com/default.aspx
http://www.qp4-example.ca/
http://www.parvenholt-example.com/Home
https://www.lumivaleholdings-example.com/index.asp
http://www.crispell-example.ca/Home_Page.html
http://www.dqrmoxley-example.com/#!contact/c16fm
http://www.fenstraleinvest-example.com/
http://www.oberlyn-example.com/
https://www.quessagroup-example.com/
http://www.mkvor-example.com/
http://www.hadrickgroup-example.com/

Don't Like
http://www.silvertallow-example.com
http://kemble-example.com/
http://rvandolin-example.com/
http://www.ptwilder-example.com/operations_team.html

Also must have a section entitles Alternative Investments

```html
<!DOCTYPE html>
<html lang="en">
<head>
<meta charset="utf-8">
<title>Velbrook Asset Management</title>
<link href="https://fonts.googleapis.com/css2?family=Questrial&family=Libre+Baskerville&display=swap" rel="stylesheet">
<style>
:root{
  --navy:#2c3a4c;
  --navy-light:#34465b;
  --teal:#1cb995;
  --teal-dark:#17a384;
  --mist:#eceff0;
  --ink:#222a33;
  --body:#666d73;
  --link:#3a86c8;
  --rule:#d9dcde;
  --white:#ffffff;
}
*{box-sizing:border-box;margin:0;padding:0}
html,body{width:937px;height:1200px;overflow:hidden;background:var(--white)}
body{font-family:"Questrial",sans-serif;color:var(--ink)}
.page{position:relative;width:937px;height:1200px;overflow:hidden}
.abs{position:absolute}

.topbar{left:0;top:0;width:937px;height:22px;background:var(--navy)}
.social{display:flex;gap:6px}
.social span{display:block;width:9px;height:9px;border-radius:50%;background:var(--white)}
.topbar .social{position:absolute;right:132px;top:6px}

.header{left:0;top:22px;width:937px;height:50px;background:var(--white)}
.brand{position:absolute;left:131px;top:11px;font-family:"Libre Baskerville",serif;font-size:24px;color:var(--ink);letter-spacing:.5px}
.nav{position:absolute;left:404px;top:0;height:50px;display:flex}
.nav a{display:flex;align-items:center;justify-content:center;text-align:center;height:50px;padding:0 12px;font-size:10px;line-height:11px;color:var(--ink);text-decoration:none;letter-spacing:.5px}
.nav a.active{background:#eeeeee;border-bottom:3px solid var(--teal);padding:3px 12px 0}

.hero{left:0;top:72px;width:937px;height:363px;background:linear-gradient(180deg,#8d8a86 0%,#b08a63 35%,#a2612c 62%,#5b3219 100%)}
.hero-line{position:absolute;left:50%;transform:translateX(-50%);color:var(--white);font-size:30px;white-space:nowrap;letter-spacing:.5px;display:flex;align-items:center;justify-content:center}
.hero-line.primary{top:129px;width:288px;height:50px;background:rgba(44,58,76,.92)}
.hero-line.secondary{top:180px;width:346px;height:51px;background:rgba(28,185,149,.92)}

.funds{left:0;top:435px;width:937px;height:312px;background:var(--mist)}
.fund{position:absolute;top:52px;width:220px;text-align:center}
.fund-icon{width:70px;height:70px;margin:0 auto;border-radius:50%;background:var(--teal);border:3px solid #7fe0c8;box-shadow:0 0 0 2px var(--teal);display:flex;align-items:center;justify-content:center;color:var(--white);font-size:28px}
.fund-title{margin-top:27px;font-size:16px;color:var(--ink)}
.fund-text{margin-top:12px;font-size:9.5px;line-height:16.4px;color:var(--body);letter-spacing:.3px}
.read-more{display:block;font-size:9.5px;color:var(--link);text-decoration:none;margin-top:1px}

.col{position:absolute;top:800px}
.col-head{position:relative;font-size:16px;color:var(--ink);height:20px;border-bottom:1px solid var(--rule)}
.col-head::after{content:"";position:absolute;left:0;bottom:-1px;width:22px;height:2px;background:var(--teal)}
.col-head .more{position:absolute;right:0;top:5px;font-size:9px;color:#b0b4b7}
.about{left:140px;width:180px}
.about p{margin-top:17px;font-size:9.5px;line-height:17px;color:var(--body)}
.about p+p{margin-top:14px}
.about .read-more{text-align:right;margin-top:8px}
.media{left:380px;width:185px}
.media ul{list-style:none;margin-top:13px}
.media li{position:relative;padding-left:11px;margin-bottom:5px}
.media li::before{content:"";position:absolute;left:0;top:3px;border-left:5px solid var(--teal);border-top:3px solid transparent;border-bottom:3px solid transparent}
.media .headline{font-size:9.5px;line-height:17px;color:var(--ink);text-transform:uppercase}
.media .source{font-size:7px;color:var(--body);margin-top:1px}
.newsletter{left:603px;width:190px}
.newsletter .intro{margin-top:14px;margin-left:-5px;font-size:9.5px;line-height:17px;color:var(--body)}
.field{margin-top:7px;margin-left:1px;width:190px;height:24px;border:1px solid #c9cdd0;border-radius:2px;font-size:8px;color:var(--body);padding:6px 5px}
.field.tall{height:45px}
.submit{margin-top:8px;margin-left:133px;width:58px;height:23px;background:var(--teal);color:var(--white);font-size:8.5px;display:flex;align-items:center;justify-content:center;letter-spacing:.5px}

.social-band{left:0;top:1100px;width:937px;height:31px;background:var(--teal);display:flex;align-items:center;justify-content:center;gap:8px;color:var(--white);font-size:8.5px;letter-spacing:.5px}
.social-band .social span{width:8px;height:8px}
.footer-nav{left:0;top:1131px;width:937px;height:42px;background:var(--navy);display:flex;align-items:center;justify-content:center;gap:9px}
.footer-nav a{color:var(--white);font-size:8.5px;text-decoration:none;letter-spacing:.3px}
.footer-bottom{left:0;top:1173px;width:937px;height:27px;background:var(--navy-light);font-size:8.5px;color:#8fa1b3;letter-spacing:.6px}
.footer-bottom .copy{position:absolute;left:124px;top:9px}
.footer-bottom .disclaimer{position:absolute;right:129px;top:9px;color:#c6d0da}
</style>
</head>
<body>
<div class="page">
  <div class="abs topbar">
    <div class="social" aria-label="Social links"><span></span><span></span><span></span></div>
  </div>

  <header class="abs header">
    <div class="brand">Velbrook</div>
    <nav class="nav">
      <a class="active" href="#">HOME</a>
      <a href="#">PROFILE</a>
      <a href="#">INVESTMENT<br>PROCCESS</a>
      <a href="#">INVESTMENT<br>SOLUTIONS</a>
      <a href="#">NEWS<br>&amp; VIEWS</a>
      <a href="#">CONTACT</a>
    </nav>
  </header>

  <section class="abs hero" role="img" aria-label="Photograph of a hiker standing on a mountain ridge at sunset">
    <div class="hero-line primary">Growing Wealth</div>
    <div class="hero-line secondary">Preserving Capital</div>
  </section>

  <section class="abs funds">
    <div class="fund" style="left:129px">
      <div class="fund-icon">$</div>
      <h3 class="fund-title">Dividend &amp; Income Fund</h3>
      <p class="fund-text">Lorem Ipsum is simply dummy text of the printing and typesetting industry. Lorem Ipsum has been the industry's standard dummy text ever since the 1500s.</p>
      <a class="read-more" href="#">Read More &gt;&gt;</a>
    </div>
    <div class="fund" style="left:359px">
      <div class="fund-icon">
        <svg width="26" height="26" viewBox="0 0 24 24" aria-hidden="true"><polygon fill="#fff" points="12,1.5 15,9 23,9.2 16.7,14 19,22 12,17.3 5,22 7.3,14 1,9.2 9,9"/></svg>
      </div>
      <h3 class="fund-title">Enhanced Equity Fund</h3>
      <p class="fund-text">Lorem Ipsum is simply dummy text of the printing and typesetting industry. Lorem Ipsum has been the industry's standard dummy text ever since the 1500s.</p>
      <a class="read-more" href="#">Read More &gt;&gt;</a>
    </div>
    <div class="fund" style="left:590px">
      <div class="fund-icon" style="font-style:italic;font-family:'Libre Baskerville',serif">α</div>
      <h3 class="fund-title">Alpha Fund</h3>
      <p class="fund-text">Lorem Ipsum is simply dummy text of the printing and typesetting industry. Lorem Ipsum has been the industry's standard dummy text ever since the 1500s.</p>
      <a class="read-more" href="#">Read More &gt;&gt;</a>
    </div>
  </section>

  <section class="col about">
    <h3 class="col-head">About</h3>
    <p>&nbsp;Velbrook serves the investment needs of individuals and their families, trusts and estates, endowments and foundations, and pensions and institutions.</p>
    <p>&nbsp;Clients are provided with comprehensive reporting, inclusive of performance reporting and market commentary. We are always available and encourage regular review meetings.</p>
    <a class="read-more" href="#">Read more&gt;&gt;</a>
  </section>

  <section class="col media">
    <h3 class="col-head">Media <span class="more">More&gt;&gt;</span></h3>
    <ul>
      <li><div class="headline">Shifting to cash for safety</div><div class="source">Ledger Daily, May 23, 2012</div></li>
      <li><div class="headline">Roller coaster week ends almost where it began</div><div class="source">Ledger Daily, August 13, 2011</div></li>
      <li><div class="headline">A risky haven</div><div class="source">Ledger Daily, August 6, 2011</div></li>
      <li><div class="headline">It's not 2008, really</div><div class="source">Ledger Daily, August 6, 2011</div></li>
    </ul>
  </section>

  <section class="col newsletter">
    <h3 class="col-head">Newsletter</h3>
    <p class="intro">To receive our newsletter, The Velbrook Perspective, or any other information, please complete the form below or contact us directly:</p>
    <div class="field" style="margin-top:12px">Name:</div>
    <div class="field">Email:</div>
    <div class="field tall">Comment:</div>
    <div class="submit">SUBMIT</div>
  </section>

  <div class="abs social-band">GET SOCIAL WITH US <div class="social"><span></span><span></span><span></span></div></div>

  <nav class="abs footer-nav">
    <a href="#">HOME</a><a href="#">PROFILE</a><a href="#">INVESTMENT PROCESS</a><a href="#">INVESTMENT SOLUTIONS</a><a href="#">NEWS &amp; VIEWS</a><a href="#">CONTACT</a>
  </nav>

  <footer class="abs footer-bottom">
    <span class="copy">COPYRIGHT 2014. ALL RIGHTS RESERVED VELBROOK ASSET MANAGEMENT INC.</span>
    <span class="disclaimer">DISCLAIMER</span>
  </footer>
</div>
</body>
</html>
```